Kestrel Summit 2019 Enemies of the End-Times Church Flyer

We want a church conference flyer designed. We are looking for a professional, yet catchy design that uses our brand colors and logo creatively while communicating key information of the event effectively. <br/>The flyer must include all of the following:<br/>Title: Kestrel Summit 2019<br/>Topic: The Enemies of The End-Times Church <br/>Subtitles: <br/> -How the antichrist raises an army by social behavior engineering. <br/>-How the architects of modern social constructs escaped the church's radar. <br/>-The Holy Spirit's end-times agenda:<br/> The Knock-Out Punch!<br/>Speaker: Prophet Marcus Toliver <br/>Dates/time: December 27, 28 & 29 at 6pm<br/>Location: Halvorn Community Center <br/> 241 Pellham Street <br/> Portland, ME 04102<br/>Contact info: phone: 207-555-0148 <br/>email: contact@brookmeadow.example <br/> www.vutel.example<br/>*The flyer must also include a picture of the speaker and our Vutel logo <br/>Thanks, we look forward to seeing what you come up with!

Colors

Designer to choose colors to be used in the design.

Requirements
Must have
• The flyer must include all of the following:
• Title: Kestrel Summit 2019
• Topic: The Enemies of The End-Times Church
• Subtitles:
• -How the antichrist raises an army by social behavior engineering.
• -How the architects of modern social constructs escaped the church's radar.
• -The Holy Spirit's end-times agenda:
• The Knock-Out Punch!
• Speaker: Prophet Marcus Toliver
• Dates/time: December 27, 28 & 29 at 6pm
• Location: Halvorn Community Center
• 241 Pellham Street
• Portland, ME 04102
• Contact info: phone: 207-555-0148
• email: contact@brookmeadow.example
• www.vutel.example
• *The flyer must also include a picture of the speaker and our Vutel logo
Should not have
• Pictures of crosses or church buildings

```html
<!DOCTYPE html>
<html lang="en">
<head>
<meta charset="utf-8">
<title>Kestrel Summit 2019 – The Enemies of The End-Times Church</title>
<link href="https://fonts.googleapis.com/css2?family=Oswald:wght@400;500;600;700&display=swap" rel="stylesheet">
<style>
  :root {
    --orange: #f7931e;
    --navy: #0d3559;
    --white: #ffffff;
    --shadow: #1d2b3a;
    --page: #ffffff;
  }
  * { margin: 0; padding: 0; box-sizing: border-box; }
  html, body { width: 847px; height: 1200px; overflow: hidden; background: var(--page); }
  .canvas { position: relative; width: 847px; height: 1200px; }
  .flyer {
    position: absolute; left: 12px; top: 12px; width: 818px; height: 1148px;
    background: var(--orange); overflow: hidden;
    font-family: "Oswald", "Arial Narrow", sans-serif;
  }
  .event-bar {
    position: absolute; left: 0; top: 33px; width: 818px; height: 60px;
    background: var(--navy); color: var(--orange);
    display: flex; align-items: center; justify-content: center;
    font-size: 42px; font-weight: 500; letter-spacing: 0.5px; text-transform: uppercase;
  }
  .event-bar .year { font-weight: 400; margin-left: 12px; }
  .speaker-hero {
    position: absolute; left: 0; top: 93px; width: 350px; height: 290px;
    background: radial-gradient(ellipse at 45% 45%, #d9771a 0%, #e98a1e 45%, var(--orange) 80%);
  }
  .topic {
    position: absolute; left: 286px; top: 122px; color: var(--white);
    font-family: "Oswald", "Arial Narrow", sans-serif; font-weight: 700;
    font-size: 76px; line-height: 72px; letter-spacing: 1px;
    text-shadow: 3px 3px 0 var(--shadow);
  }
  .topic .small { font-weight: 400; font-size: 58px; letter-spacing: 0; }
  .band { position: absolute; left: 0; width: 818px; }
  .band svg { position: absolute; inset: 0; }
  .band-text {
    position: relative; color: var(--white); padding-left: 36px;
    font-size: 17px; font-weight: 500; letter-spacing: 1px;
  }
  .band-1 { top: 375px; height: 38px; }
  .band-2 { top: 421px; height: 38px; }
  .band-1 .band-text, .band-2 .band-text { line-height: 38px; }
  .band-3 { top: 468px; height: 112px; }
  .band-3 .band-text { padding-top: 12px; }
  .agenda-lead { display: block; font-size: 30px; line-height: 38px; letter-spacing: 0.8px; }
  .agenda-punch {
    display: block; color: var(--orange); font-size: 46px; line-height: 52px;
    font-weight: 700; letter-spacing: 2.5px;
  }
  .details {
    position: absolute; left: 0; top: 591px; width: 818px; height: 393px; background: var(--navy);
  }
  .info { position: absolute; left: 36px; top: 44px; }
  .info-block { margin-bottom: 10px; }
  .label { display: block; color: var(--white); font-size: 17px; font-weight: 500; line-height: 26px; }
  .value { display: block; color: var(--orange); font-size: 23px; font-weight: 600; line-height: 27px; }
  .speaker-photo {
    position: absolute; left: 538px; top: 43px; width: 243px; height: 268px;
    border: 3px solid var(--white);
    background: linear-gradient(160deg, #a7a9a4 0%, #6f6a63 45%, #3a302b 100%);
  }
  .speaker-caption { position: absolute; left: 540px; top: 320px; }
  .speaker-caption .value { font-size: 27px; line-height: 32px; }
  .brand {
    position: absolute; left: 36px; top: 1015px; width: 96px; height: 96px;
    background: var(--navy); color: var(--white);
    display: flex; align-items: center; justify-content: center;
    font-size: 24px; font-weight: 500; letter-spacing: 1px;
  }
  .web {
    position: absolute; right: 36px; top: 1090px; color: var(--navy);
    font-size: 19px; font-weight: 600;
  }
</style>
</head>
<body>
<div class="canvas">
  <article class="flyer">
    <header class="event-bar">Kestrel Summit<span class="year">2019</span></header>

    <div class="speaker-hero" role="img" aria-label="Orange duotone photo of the speaker preaching into a headset microphone"></div>

    <h1 class="topic">The Enemies <span class="small">of</span><br>The End-Times<br>Church</h1>

    <div class="band band-1">
      <svg width="818" height="38" viewBox="0 0 818 38" aria-hidden="true"><polygon points="0,0 782,0 766,38 0,38" fill="#0d3559"/></svg>
      <p class="band-text">How the antichrist raises an army by social behavior engineering.</p>
    </div>
    <div class="band band-2">
      <svg width="818" height="38" viewBox="0 0 818 38" aria-hidden="true"><polygon points="0,0 782,0 766,38 0,38" fill="#0d3559"/></svg>
      <p class="band-text">How the architects of modern social constructs escaped the church's radar.</p>
    </div>
    <div class="band band-3">
      <svg width="818" height="112" viewBox="0 0 818 112" aria-hidden="true"><polygon points="0,0 782,0 752,112 0,112" fill="#0d3559"/></svg>
      <p class="band-text"><span class="agenda-lead">The Holy Spirit's end-times agenda</span><span class="agenda-punch">The Knock-Out Punch!</span></p>
    </div>

    <section class="details">
      <div class="info">
        <div class="info-block"><span class="label">Dates/time:</span><span class="value">December 27, 28 &amp; 29 at 6pm</span></div>
        <div class="info-block"><span class="label">Location:</span><span class="value">Halvorn Community Center<br>241 Pellham Street<br>Portland,<br>ME 04102</span></div>
        <div class="info-block"><span class="label">Contact info:</span><span class="value">phone: 207-555-0148</span></div>
        <div class="info-block"><span class="label">email:</span><span class="value">contact@brookmeadow.example</span></div>
      </div>
      <div class="speaker-photo" role="img" aria-label="Portrait photo of the speaker in front of a bookshelf"></div>
      <div class="speaker-caption"><span class="label">Speaker:</span><span class="value">Prophet Marcus Toliver</span></div>
    </section>

    <div class="brand">Vutel</div>
    <p class="web">www.vutel.example</p>
  </article>
</div>
</body>
</html>
```